New Company Business Card design

Looking for a corporate looking business card utilising my new logo design - the logo i would like embossed as one option and flat as another - simplistic but stylish - less is more - we are an import export business launching into the market - i would like a couple of options as main background - Grey or Black

```html
<!DOCTYPE html>
<html lang="en">
<head>
<meta charset="utf-8">
<title>Meridian Trade Partners – Business Card</title>
<link rel="stylesheet" href="https://fonts.googleapis.com/css2?family=Cinzel:wght@400;600&family=Work+Sans:wght@400;500&display=swap">
<style>
  :root {
    --backdrop: #1b1b1c;
    --card: #1f1f21;
    --card-edge: #262628;
    --brand-blue: #1b7fd1;
    --white: #ffffff;
    --muted: #e6e6e6;
  }
  * { box-sizing: border-box; margin: 0; padding: 0; }
  html, body { width: 1200px; height: 900px; overflow: hidden; background: var(--backdrop); }
  .canvas {
    width: 1200px; height: 900px;
    display: flex; flex-direction: column; align-items: center; justify-content: center;
    gap: 50px;
  }
  .card {
    position: relative;
    width: 700px; height: 380px;
    background: linear-gradient(135deg, var(--card) 0%, var(--card-edge) 100%);
    border-bottom: 7px solid var(--brand-blue);
  }
  /* brand lockup */
  .brand { display: flex; flex-direction: column; align-items: center; }
  .brand-row { display: flex; align-items: center; gap: 14px; }
  .brand-dot { width: 26px; height: 26px; border-radius: 50%; background: var(--brand-blue); }
  .brand-name {
    font-family: "Work Sans", sans-serif; font-weight: 500;
    color: var(--brand-blue); letter-spacing: 0.06em; text-transform: uppercase;
    font-size: 30px;
  }
  .brand-rule { width: 100%; height: 1px; background: var(--white); margin: 12px 0 8px; }
  .brand-tagline {
    font-family: "Cinzel", serif; font-size: 12px; letter-spacing: 0.32em;
    color: var(--white); text-transform: uppercase;
  }
  .card--front { display: flex; align-items: center; justify-content: center; }
  .card--front .brand-name { font-size: 34px; }

  .card--back { display: flex; align-items: center; padding: 0 40px; }
  .card--back .brand { width: 330px; }
  .card--back .brand-name { font-size: 22px; }
  .card--back .brand-tagline { font-size: 9.5px; letter-spacing: 0.26em; }
  .divider { width: 2px; height: 180px; background: var(--white); margin: 0 34px 0 34px; }
  .contact { font-family: "Work Sans", sans-serif; color: var(--muted); }
  .contact-name { color: var(--brand-blue); font-size: 27px; font-weight: 500; text-transform: uppercase; letter-spacing: 0.02em; }
  .contact-role { font-size: 17px; margin-bottom: 18px; }
  .contact-address { font-size: 17px; line-height: 1.35; margin-bottom: 10px; }
  .contact-line { display: flex; align-items: center; gap: 10px; font-size: 18px; line-height: 1.4; }
  .contact-line svg { width: 14px; height: 14px; flex: none; }
  .accent { color: var(--brand-blue); }
</style>
</head>
<body>
<main class="canvas">
  <section class="card card--front">
    <div class="brand">
      <div class="brand-row">
        <span class="brand-dot"></span>
        <span class="brand-name">Meridian Trade Partners</span>
      </div>
      <div class="brand-rule"></div>
      <p class="brand-tagline">Worldwide supply for every market</p>
    </div>
  </section>

  <section class="card card--back">
    <div class="brand">
      <div class="brand-row">
        <span class="brand-dot"></span>
        <span class="brand-name">Meridian Trade Partners</span>
      </div>
      <div class="brand-rule"></div>
      <p class="brand-tagline">Worldwide supply for every market</p>
    </div>
    <div class="divider"></div>
    <div class="contact">
      <h1 class="contact-name">Daniel Reyes</h1>
      <p class="contact-role">Director</p>
      <p class="contact-address">2250 Harbor View Ave<br>Linden, CA 95236-4410</p>
      <p class="contact-line">
        <svg viewBox="0 0 16 16" fill="none" stroke="#1b7fd1" stroke-width="1.6"><path d="M3 2h3l1 3-2 1.5a9 9 0 0 0 4.5 4.5L11 9l3 1v3a1 1 0 0 1-1 1A12 12 0 0 1 2 3a1 1 0 0 1 1-1z"/></svg>
        555-204-7731
      </p>
      <p class="contact-line">
        <svg viewBox="0 0 16 16" fill="none" stroke="#1b7fd1" stroke-width="1.4"><rect x="1.5" y="3.5" width="13" height="9"/><path d="M1.5 3.5 8 9l6.5-5.5"/></svg>
        hello@meridiantrade.com
      </p>
      <p class="contact-line">
        <svg viewBox="0 0 16 16" fill="none" stroke="#1b7fd1" stroke-width="1.3"><circle cx="8" cy="8" r="6.5"/><ellipse cx="8" cy="8" rx="3" ry="6.5"/><path d="M1.5 8h13"/></svg>
        <span>www.<span class="accent">meridiantrade</span>.com</span>
      </p>
    </div>
  </section>
</main>
</body>
</html>
```